Urkundendesign für Jahrgangsbeste einer Realschule gesucht
Zielgruppe
Der Elternbeirat der Realschule Felkenried benötigt für die Jahrgangsbesten des Abschlussjahrgangs eine Urkunde. Gerne mit Prägung (was kostet sowas bei Druck?!?). Das von-Haltmoor-Logo darf benutzt werden (siehe Homepage).
es soll eine Urkunde für den/die 'Jahrgangsbeste 2026' geben. das Datum, sowie SchülerInnen-Name würden wir jeweils handschriftlich anbringen.
die Urkunde in A4 gestalten.
wir benötigen die üblichen druckbaren Dateien, sodass eine Druckerei dann auch selbst Jahr für Jahr das Jahr abändern kann.
Aufgabenstellung
bitte um Vorschläge, wir arbeiten uns nach und nach da durch.
nicht zu viel Schnörkelei.

```html
<!DOCTYPE html>
<html lang="de">
<head>
<meta charset="utf-8">
<title>Urkunde Jahrgangsbeste 2026</title>
<link rel="stylesheet" href="https://fonts.googleapis.com/css2?family=Gelasio:wght@400;700&family=Arimo:wght@400;700&display=swap">
<style>
  :root {
    --page: #ffffff;
    --paper: #faf8f4;
    --gold: #d4ae3c;
    --gold-light: #f5dc8e;
    --gold-dark: #c49a25;
    --navy: #1b2540;
    --ink: #1c1c1c;
    --rule: #2a3350;
  }
  html, body {
    margin: 0;
    padding: 0;
    width: 1200px;
    height: 1199px;
    overflow: hidden;
    background: var(--page);
  }
  .canvas {
    position: relative;
    width: 1200px;
    height: 1199px;
    font-family: "Arimo", Arial, sans-serif;
    color: var(--ink);
  }
  .certificate-frame {
    position: absolute;
    left: 0; top: 0;
  }
  .line {
    position: absolute;
    margin: 0;
    white-space: nowrap;
  }
  .centered {
    left: 593px;
    transform: translateX(-50%);
    text-align: center;
  }
  .school-name {
    top: 106px;
    font-size: 14.5px;
    font-weight: 700;
    letter-spacing: 1.3px;
    color: var(--ink);
  }
  .brand-mark {
    top: 158px;
    display: flex;
    align-items: center;
    gap: 8px;
    font-size: 20px;
    font-weight: 700;
    color: var(--navy);
  }
  .brand-mark .dot {
    width: 14px; height: 14px;
    border-radius: 50%;
    background: var(--gold);
  }
  .school-title {
    top: 245px;
    font-size: 21px;
    font-weight: 700;
    letter-spacing: 1.6px;
    color: var(--navy);
  }
  .awarded-by {
    top: 277px;
    font-size: 14.5px;
    letter-spacing: 0.6px;
    color: #333;
  }
  .heading {
    top: 323px;
    font-family: "Gelasio", Georgia, serif;
    font-size: 86px;
    letter-spacing: 14px;
    padding-left: 14px;
    color: var(--navy);
    line-height: 1;
  }
  .subheading {
    top: 440px;
    font-family: "Gelasio", Georgia, serif;
    font-size: 29px;
    letter-spacing: 2px;
    line-height: 44px;
    color: var(--navy);
  }
  .award-band {
    position: absolute;
    left: 307px;
    top: 552px;
    width: 573px;
    height: 74px;
  }
  .award-band svg { position: absolute; inset: 0; }
  .award-band span {
    position: absolute;
    inset: 0;
    display: flex;
    align-items: center;
    justify-content: center;
    font-family: "Gelasio", Georgia, serif;
    font-weight: 700;
    font-size: 37px;
    letter-spacing: 1px;
    color: var(--navy);
  }
  .citation {
    top: 659px;
    font-size: 19px;
    line-height: 31px;
  }
  .recipient-label {
    left: 371px;
    top: 768px;
    font-size: 24px;
    color: var(--navy);
  }
  .recipient-rule {
    position: absolute;
    left: 423px;
    top: 790px;
    width: 435px;
    border-top: 2px solid var(--rule);
  }
  .class-info { font-size: 19px; }
  .class-info.first { left: 396px; top: 831px; }
  .class-info.second { left: 331px; top: 861px; }
  .place-date {
    left: 312px;
    top: 938px;
    font-size: 19px;
  }
  .signature-title {
    top: 1004px;
    font-size: 16.5px;
    transform: translateX(-50%);
  }
  .signature-title.principal { left: 433px; }
  .signature-title.board { left: 752px; }
  .signature-rule {
    position: absolute;
    top: 1093px;
    width: 275px;
    border-top: 2px solid var(--rule);
  }
  .signature-rule.principal { left: 296px; }
  .signature-rule.board { left: 614px; }
  .signature-caption {
    top: 1105px;
    font-size: 15px;
    transform: translateX(-50%);
  }
  .signature-caption.principal { left: 433px; }
  .signature-caption.board { left: 752px; }
</style>
</head>
<body>
<main class="canvas">
  <svg class="certificate-frame" width="1200" height="1199" viewBox="0 0 1200 1199" aria-hidden="true">
    <polygon points="232,48 955,48 971,64 971,1136 955,1152 232,1152 216,1136 216,64"
             fill="var(--paper)" stroke="var(--gold)" stroke-width="2"/>
    <polygon points="240,58 947,58 960,71 960,1129 947,1142 240,1142 227,1129 227,71"
             fill="none" stroke="var(--gold)" stroke-width="1"/>
  </svg>

  <p class="line centered school-name">STAATLICHE REALSCHULE FELKENRIED</p>
  <div class="line centered brand-mark"><span class="dot"></span>von-Haltmoor</div>
  <p class="line centered school-title">VON-HALTMOOR-REALSCHULE</p>
  <p class="line centered awarded-by">VERLIEHEN VOM ELTERNBEIRAT</p>

  <h1 class="line centered heading">URKUNDE</h1>
  <p class="line centered subheading">FÜR DIE JAHRGANGSBESTE /<br>DEN JAHRGANGSBESTEN</p>

  <div class="award-band">
    <svg width="573" height="74" viewBox="0 0 573 74" aria-hidden="true">
      <defs>
        <linearGradient id="goldBand" x1="0" y1="0" x2="1" y2="1">
          <stop offset="0" stop-color="var(--gold-dark)"/>
          <stop offset="0.45" stop-color="var(--gold-light)"/>
          <stop offset="0.6" stop-color="#f0d27e"/>
          <stop offset="1" stop-color="var(--gold-dark)"/>
        </linearGradient>
      </defs>
      <polygon points="14,0 559,0 573,14 573,60 559,74 14,74 0,60 0,14" fill="url(#goldBand)"/>
    </svg>
    <span>JAHRGANGSBESTE 2026</span>
  </div>

  <p class="line centered citation">als Anerkennung für herausragende schulische<br>Leistungen und besonderes Engagement.</p>

  <p class="line recipient-label">an:</p>
  <div class="recipient-rule"></div>

  <p class="line class-info first">als Jahrgangsbeste/r der Abschlussklasse</p>
  <p class="line class-info second">im Schuljahr2025/2026</p>

  <p class="line place-date">Felkenried, den.....</p>

  <p class="line signature-title principal">Der Schulleiter</p>
  <p class="line signature-title board">Der Vorsitzende des Elternbeirats</p>
  <div class="signature-rule principal"></div>
  <div class="signature-rule board"></div>
  <p class="line signature-caption principal">Name, Unterschrift</p>
  <p class="line signature-caption board">Name, Unterschrift</p>
</main>
</body>
</html>
```